Vesprine Oakville Cabernet Sauvignon-Wine label design

We need a package design for an up market wine brand named, Vesprine. It will be a Cabernet Sauvignon from the Oakville AVA of Napa Valley. We are looking for a stylish modern label that will stand out on a retail shelf. We want the label to be attention grabbing and stylish while presenting an up market luxury brand.

Sick

Requirements
Must have
• Must have the words(in order of importance)
-Vesprine
-Cabernet Sauvignon
-Oakville
-Napa Valley
-2018

Must be designed for a traditional "Bordeaux" style bottle (Bottle specs in uploaded files)
Should not have
• Any images of grapes, vineyards, wine glasses or bottles

```html
<!DOCTYPE html>
<html lang="en">
<head>
<meta charset="utf-8">
<title>Vesprine Oakville Cabernet Sauvignon — Label</title>
<link rel="stylesheet" href="https://fonts.googleapis.com/css2?family=Bodoni+Moda:wght@400;500&display=swap">
<style>
  :root {
    --page: #ffffff;
    --label-black: #07090a;
    --sheen: rgba(120, 130, 132, 0.28);
    --sheen-faint: rgba(90, 98, 100, 0.12);
    --gold: #f2a900;
    --gold-glow: rgba(242, 169, 0, 0.30);
    --gold-faint: rgba(242, 169, 0, 0.06);
    --ivory: #ffffff;
  }
  * { margin: 0; padding: 0; box-sizing: border-box; }
  html, body {
    width: 869px;
    height: 1200px;
    overflow: hidden;
    background: var(--page);
  }
  .canvas {
    position: relative;
    width: 869px;
    height: 1200px;
  }
  .label {
    position: absolute;
    left: 104px;
    top: 0;
    width: 662px;
    height: 1200px;
    background: var(--label-black);
    overflow: hidden;
    font-family: "Bodoni Moda", "Didot", serif;
    text-align: center;
  }
  .label__backdrop {
    position: absolute;
    inset: 0;
    background:
      radial-gradient(ellipse 55% 30% at 70% 18%, var(--sheen), transparent 70%),
      radial-gradient(ellipse 40% 35% at 15% 75%, var(--sheen-faint), transparent 70%),
      radial-gradient(ellipse 60% 20% at 55% 95%, var(--sheen-faint), transparent 70%);
  }
  .label__monogram {
    position: absolute;
    left: 24px;
    top: 165px;
    width: 618px;
    height: 660px;
    border-radius: 50%;
    background: radial-gradient(ellipse at 50% 50%, var(--gold-glow), var(--gold-faint) 60%, transparent 72%);
  }
  .brand-name {
    position: absolute;
    left: 0;
    right: 0;
    top: 460px;
    font-weight: 500;
    font-size: 110px;
    line-height: 1;
    letter-spacing: -0.01em;
    color: var(--ivory);
  }
  .varietal {
    position: absolute;
    left: 0;
    right: 0;
    color: var(--gold);
    font-weight: 400;
    line-height: 1;
    font-size: 50px;
  }
  .varietal--first {
    top: 862px;
    letter-spacing: 0.62em;
    padding-left: 0.62em;
  }
  .varietal--second {
    top: 936px;
    letter-spacing: 0.5em;
    padding-left: 0.5em;
  }
  .appellation {
    position: absolute;
    left: 0;
    right: 0;
    top: 1112px;
    display: flex;
    justify-content: center;
    align-items: baseline;
    gap: 10px;
    color: var(--gold);
    line-height: 1;
  }
  .appellation__place {
    font-size: 25px;
    letter-spacing: 0.12em;
  }
  .appellation__vintage {
    font-size: 50px;
    font-weight: 500;
  }
</style>
</head>
<body>
  <main class="canvas">
    <section class="label">
      <div class="label__backdrop" role="img" aria-label="Soft grey silk ribbons sweeping across a black background"></div>
      <div class="label__monogram" role="img" aria-label="Large gold script monogram ornament"></div>

      <h1 class="brand-name">VESPRINE</h1>
      <p class="varietal varietal--first">CABERNET</p>
      <p class="varietal varietal--second">SAUVIGNON</p>
      <p class="appellation">
        <span class="appellation__place">OAKVILLE</span>
        <span class="appellation__vintage">2018</span>
        <span class="appellation__place">NAPA VALLEY</span>
      </p>
    </section>
  </main>
</body>
</html>
```